We are looking to improve our packaging, because we are wanting to secure our products into five star hotels, spa and wellness centres and maybe even high end retail department stores. That is why it is important it must look the part. We are even prepared to change our current packaging (White stand up pouches) for something different e.g box etc...

Please keep in mind when designing our new Serenwell packaging that our product range will extend to Room Sprays, Candles, Diffuser, Essential Oils, Soaps, Body Scrubs, Milk Baths, Body Lotions, Face Products. So the design will need to compliment and we must be able to adjust the artwork with ease to fit bottles big and small, tubes, boxes glass jars etc... at later stage.

Please see inspiration images of packaging I like. But please do not copy them. We would like something that is unique to our brand that will last for 2-4 years before we have to change the packaging again.

Our current packaging is in a white stand up pouches.
Updates

Project Deadline Extended Reason: Hi All,I have decided to extend the Serenwell Calm Mix Packaging project as the designs I have received are not what I am looking for and are not polished enough for the retail health and spa market. Some of the ideas I received are on the right track, but they need to be reworked a bit more to give our packaging a premium high end looking product. I am trying to get our products into large retail outlets department stores, Chemists, Health and natural product stores, 5 star spa resorts and hotels and eventually export it globally and with so many similar products available for sale our products needs to stand out from the rest of the competition. We use premium grade salts with natural and organic ingredients in our products when we make them. They do not have any harsh chemicals in them. At the moment I am keeping to the stand up white pouches for now, but this will change later this year to a box. We have a good product that sells well, but our current look and feel of our packaging is letting us down and making it difficult to market into the bigger retail stores. I have attached a few sample ideas of what we like, but with our own unique mark to it. We would like something that is unique to us to give our Serenwell brand its own identity. I will leave this up to your creative skills.Our Serenwell product range will branch out to the following in a couple of months. Body Scrubs, Liquid Soaps, Soaps, Body and Face Lotions, Milk baths, Bath and Spa Tea Bags, Bubble Paths, Herbal and Fragranced Bath & Spa products, Steam Therapy, Massage and Bath Oils, Room Sprays, Home Fragrances and Essential oils. So please keep this mind when designing a label that it must be easily adapted to different shapes and size products. e.g. boxes, jars, tubes and bottles.If you have any question before you start, please send me a message.Thank you for taking the time to read our extended brief and very excited to see your designs. Kind Regards, Added Saturday, January 9, 2016

Target Market(s)

Male and female, natural products, well-being, holistic, wellness centres, spa resorts, 5 stars hotels and upmarket.

Industry/Entity Type

Health And Wellness

Font styles to use
Serif
Sans Serif
Other font styles liked:
• Open Sans

Requirements
Must have
• Front: Company Name: Brand name Serenwell Calm Mix (See logo attached or feel fry to add your design flair to this). Please insert Front Packaging copy, 100% pure & natural logo, weight of item 1kg
• Back: Palvex logo (attached), Australian Packed & Owned logo (attached or you can just use type), Please use Back Packaging copy attached. Please allow space for barcode, Batch number and expiry date.
Nice to have
• Vector background, natural earthy feel, natural or organic textures
• but we are open to any suggestions you might have.

```html
<!DOCTYPE html>
<html lang="en">
<head>
<meta charset="utf-8">
<title>Serenwell Calm Mix – Pouch Label</title>
<link rel="stylesheet" href="https://fonts.googleapis.com/css2?family=Open+Sans:wght@600;700&family=Bitter:ital,wght@1,600&display=swap">
<style>
  :root {
    --paper: #ffffff;
    --paper-shade: #ececec;
    --petal: #f4f4f4;
    --petal-shadow: #d2d2d2;
    --magenta: #e0247f;
    --plum: #6a2a8c;
    --violet: #7b2f9e;
    --blush: #f3b6d0;
    --seal-green: #6fbf3c;
    --seal-ribbon: #c81f6a;
    --mark-green: #1f7a3a;
    --mark-gold: #f2b705;
    --white: #ffffff;
  }
  * { margin: 0; padding: 0; box-sizing: border-box; }
  html, body { width: 877px; height: 1200px; overflow: hidden; background: var(--paper); }
  .label {
    position: relative;
    width: 877px;
    height: 1200px;
    overflow: hidden;
    background: radial-gradient(ellipse at 50% 40%, var(--paper) 40%, var(--paper-shade) 100%);
  }
  .flower {
    position: absolute;
    border-radius: 50%;
    background: radial-gradient(circle at 50% 45%, var(--paper) 0%, var(--petal) 45%, var(--petal-shadow) 75%, transparent 76%);
    opacity: .9;
  }
  .flower--top-left { left: -40px; top: -30px; width: 280px; height: 270px; }
  .flower--top-right { left: 540px; top: -40px; width: 380px; height: 470px; }
  .flower--centre { left: 205px; top: 295px; width: 230px; height: 225px; }
  .flower--left { left: -70px; top: 370px; width: 220px; height: 340px; }
  .flower--bottom-left { left: 60px; top: 770px; width: 330px; height: 260px; }

  .product-name {
    position: absolute;
    top: 120px;
    left: 0;
    width: 100%;
    text-align: center;
    font-family: "Open Sans", sans-serif;
    font-weight: 600;
  }
  .product-name__brand {
    display: block;
    font-size: 98px;
    line-height: 1;
    letter-spacing: 1px;
    background: linear-gradient(180deg, var(--magenta) 0%, var(--plum) 100%);
    -webkit-background-clip: text;
    background-clip: text;
    color: transparent;
  }
  .product-name__range {
    display: block;
    margin-top: 18px;
    font-size: 62px;
    line-height: 1;
    background: linear-gradient(180deg, var(--magenta) 0%, var(--plum) 100%);
    -webkit-background-clip: text;
    background-clip: text;
    color: transparent;
  }
  .description {
    position: absolute;
    right: 45px;
    top: 530px;
    width: 760px;
    text-align: right;
    font-family: "Bitter", serif;
    font-style: italic;
    font-weight: 600;
    font-size: 32px;
    line-height: 41px;
    color: var(--plum);
  }
  .description .ingredient { color: var(--magenta); }

  .footer-wave { position: absolute; left: 0; top: 0; }
  .seal {
    position: absolute;
    left: 98px;
    top: 1015px;
    width: 140px;
    height: 140px;
    border-radius: 50%;
    background: var(--white);
    border: 10px solid var(--seal-green);
  }
  .weight {
    position: absolute;
    left: 430px;
    top: 1134px;
    font-family: "Open Sans", sans-serif;
    font-weight: 700;
    font-size: 33px;
    color: var(--white);
  }
  .origin-mark {
    position: absolute;
    left: 640px;
    top: 1050px;
    width: 112px;
    height: 120px;
    border-radius: 6px;
    background: var(--mark-green);
    border: 4px solid var(--white);
  }
</style>
</head>
<body>
  <main class="label">
    <div class="flower flower--top-left" role="img" aria-label="White paper-cut flower with water droplets"></div>
    <div class="flower flower--top-right" role="img" aria-label="Large white paper-cut flowers with water droplets"></div>
    <div class="flower flower--centre" role="img" aria-label="White paper-cut flower"></div>
    <div class="flower flower--left" role="img" aria-label="White paper-cut flower at the left edge"></div>
    <div class="flower flower--bottom-left" role="img" aria-label="White paper-cut flower with water droplets"></div>

    <h1 class="product-name">
      <span class="product-name__brand">SERENWELL</span>
      <span class="product-name__range">CALM MIX</span>
    </h1>

    <p class="description">
      A unique blend of<br>
      <span class="ingredient">Himalayan Salt,</span><br>
      <span class="ingredient">Magnesium Chloride Flakes</span><br>
      <span class="ingredient">and Vitamin C</span><br>
      for the ultimate therapeutic bath soak.<br>
      Our Serenwell Calm Mix<br>
      will detoxify and revitalise<br>
      your body.
    </p>

    <svg class="footer-wave" width="877" height="1200" viewBox="0 0 877 1200" aria-hidden="true">
      <defs>
        <linearGradient id="band-fill" x1="0" y1="0" x2="1" y2="1">
          <stop offset="0" stop-color="#e0247f"/>
          <stop offset="1" stop-color="#6a2a8c"/>
        </linearGradient>
      </defs>
      <path d="M0 1000 C200 1040 420 1010 600 960 C720 930 810 925 877 930 L877 1200 L0 1200 Z" fill="#f3b6d0"/>
      <path d="M0 1020 C220 1070 430 1040 610 985 C730 950 815 945 877 950 L877 1200 L0 1200 Z" fill="#e0247f"/>
      <path d="M0 1060 C240 1110 450 1080 630 1020 C740 985 820 980 877 985 L877 1200 L0 1200 Z" fill="url(#band-fill)"/>
      <path d="M260 1150 C450 1110 620 1050 877 1010" stroke="#ffffff" stroke-opacity=".35" stroke-width="3" fill="none"/>
    </svg>

    <div class="seal" aria-label="Pure and natural seal"></div>
    <span class="weight">1kg</span>
    <div class="origin-mark" aria-label="Country of origin mark"></div>
  </main>
</body>
</html>
```